Need a landing page design updated

Need an existing landing page perfected, want it too look similar to one of Quenbrook's landing pages in that it flows and is really aesthetically pleasing. The link to the landing page is below. I need this design updated asap. Please take the content directly from the page.

http://verdanthollowsx.com/residential-services/

Target Market(s)

High end residential landscape customers on the gulf coast of Florida (Clearwater area)

Industry/Entity Type

Landscape Gardening

Font styles to use
Sans Serif
Decorative

Requirements
Must have
• I want to keep the written content the same on on the landing page, but would like to work on making both aesthetically appealing to the consumer. This is for high end residential clients on the gulf coast of florida, so think palm trees and sunny beaches with beautiful houses and gorgeous landscapes....look through www.verdanthollowsx.com home page for an example of the houses we landscape.
Nice to have
• Would like it to flow as you scroll similar to Quenbrook's landing pages.
• Look at how Quenbrook's landing page flows, want similar here.....
• https://www.quenbrook.com/tavlo-q/
Should not have
• this landing page must be beautiful and must make a lot of sense as you scroll, am looking for a work of art....please do not submit generic templates or anything that can be easily done....I need real artistry.

```html
<!DOCTYPE html>
<html lang="en">
<head>
<meta charset="utf-8">
<title>Verdant Hollow — Residential Landscaping</title>
<link href="https://fonts.googleapis.com/css2?family=Lato:wght@400;700;900&family=Open+Sans:wght@400;600&display=swap" rel="stylesheet">
<style>
:root{
  --teal:#1aa5cf;
  --teal-dark:#0f86ad;
  --navy:#1d2a3a;
  --ink:#2b2b2b;
  --muted:#5a5a5a;
  --line:#dcdcdc;
  --white:#ffffff;
  --soft:#f4f6f7;
  --icon-grey:#555a60;
}
*{box-sizing:border-box;margin:0;padding:0}
html,body{width:1200px;height:4627px;overflow:hidden}
body{font-family:"Open Sans",Arial,sans-serif;color:var(--ink);background:var(--white);position:relative}
section,header,footer,nav{position:relative;width:1200px}
.photo{position:absolute}

/* header */
.site-header{height:68px;background:var(--white)}
.brand{position:absolute;left:92px;top:16px;display:flex;align-items:center;gap:10px;font-family:"Lato",sans-serif;font-weight:700;font-size:26px;color:var(--navy);letter-spacing:1px}
.brand-dot{width:14px;height:14px;border-radius:50%;background:var(--teal)}
.header-contact{position:absolute;right:80px;top:18px;font-size:12px;line-height:17px;color:var(--ink)}
.header-contact .call{color:var(--teal)}
.main-nav{height:40px;background:var(--teal);display:flex;align-items:center;padding-left:96px;gap:30px}
.main-nav a{color:var(--white);text-decoration:none;font-family:"Lato",sans-serif;font-weight:700;font-size:12px;letter-spacing:.5px}

/* hero */
.hero{height:540px;overflow:hidden}
.hero-bg{inset:0;background:linear-gradient(180deg,#3d86c4 0%,#7fb9e3 45%,#5aa18e 62%,#1fa2b4 78%,#8fd3dc 100%)}
.hero-title{position:absolute;top:232px;width:100%;text-align:center;font-family:"Lato",sans-serif;font-weight:700;font-size:64px;color:var(--white);letter-spacing:2px}
.hero-lead{position:absolute;top:318px;left:180px;width:840px;text-align:center;font-size:22px;line-height:32px;color:var(--white)}
.dots{position:absolute;top:424px;width:100%;display:flex;justify-content:center;gap:8px}
.dots span{width:12px;height:12px;border-radius:50%;border:2px solid var(--white)}
.dots span.on{background:var(--white)}
.hero-wave{position:absolute;left:0;bottom:0}

/* intro */
.intro{height:430px}
.intro-text{position:absolute;left:98px;top:124px;width:520px;font-size:15.5px;line-height:28px;color:var(--ink)}
.photo-beach{left:628px;top:150px;width:226px;height:215px;background:linear-gradient(180deg,#8ec5e8,#cfe3ee 45%,#3f8fb0 60%,#d9c4a0 100%)}
.photo-cove{left:873px;top:56px;width:226px;height:217px;background:linear-gradient(180deg,#9fd2f0,#4a9d64 45%,#23a6bf 70%,#e9dcc0 100%)}

/* band */
.coast-band{height:295px;display:flex;align-items:center;justify-content:center}
.coast-band .photo{inset:0;background:linear-gradient(180deg,#3e5a3a,#2c6f77 55%,#1e7e95 100%)}
.coast-band p{position:relative;width:720px;text-align:center;font-size:21px;line-height:31px;color:var(--white)}

/* compare cards */
.compare{height:770px}
.card{position:absolute;top:90px;width:460px;height:672px;background:var(--white);border:1px solid var(--line)}
.card-generic{left:100px}
.card-tailored{left:628px}
.card .photo{left:-1px;top:-1px;width:460px;height:372px}
.card-generic .photo{background:linear-gradient(180deg,#6fb6e6,#9fd0e8 45%,#4c8a4a 70%,#69a84a 100%)}
.card-tailored .photo{background:linear-gradient(180deg,#8cbfe2,#b9a27d 50%,#4f8a3e 78%,#6aac45 100%)}
.card-body{position:absolute;top:372px;left:0;right:0;padding:34px 56px 0}
.card h2{font-family:"Lato",sans-serif;font-weight:700;font-size:24px;color:var(--ink);margin-bottom:22px}
.card ul{list-style:none}
.card li{position:relative;padding-left:24px;font-size:13px;line-height:20px;color:var(--muted);margin-bottom:18px}
.card li svg{position:absolute;left:0;top:3px}

/* eco band */
.eco-band{height:345px;text-align:center}
.eco-band .photo{inset:0;background:linear-gradient(180deg,#3b3428,#465038 45%,#3f7a2e 75%,#4d8d35 100%)}
.eco-band h2{position:relative;padding-top:78px;width:960px;margin:0 auto;font-family:"Lato",sans-serif;font-weight:700;font-size:30px;line-height:40px;color:var(--white)}
.eco-band p{position:relative;width:840px;margin:18px auto 0;font-size:15px;line-height:26px;color:#eef2ea}

/* benefits */
.benefits{height:494px}
.benefits h2{position:absolute;top:74px;width:100%;text-align:center;font-family:"Lato",sans-serif;font-weight:700;font-size:30px;color:var(--ink)}
.benefit{position:absolute;top:170px;width:308px;height:194px;border:2px solid var(--line);text-align:center;padding:106px 34px 0;font-size:13.5px;line-height:22px;color:var(--muted)}
.benefit.b1{left:100px}.benefit.b2{left:445px;border-color:var(--teal);color:var(--teal)}.benefit.b3{left:790px}
.benefit .icon{position:absolute;left:50%;top:-56px;margin-left:-58px;width:116px;height:116px;border-radius:50%;background:var(--icon-grey);display:flex;align-items:center;justify-content:center}
.benefit.b2 .icon{background:var(--teal)}

/* flaws */
.flaws{height:309px;overflow:hidden}
.flaws .photo{inset:0;background:linear-gradient(90deg,#1f6fb3 0%,#3f8ed0 45%,#7cb2d8 68%,#c7b48a 82%,#6c8e52 100%)}
.flaws h2{position:absolute;left:98px;top:72px;font-family:"Lato",sans-serif;font-weight:700;font-size:30px;line-height:38px;color:var(--white)}
.flaws ol{position:absolute;left:98px;top:160px;list-style:none;font-size:15px;line-height:25px;color:var(--white)}

/* testimonials */
.testimonials{height:764px;text-align:center}
.testimonials h2{position:absolute;top:70px;width:100%;font-family:"Lato",sans-serif;font-weight:700;font-size:30px;line-height:38px;color:var(--ink)}
.testimonials .photo{left:302px;top:178px;width:598px;height:346px;background:linear-gradient(180deg,#8ec8ef,#dfe8ea 45%,#5a9a4c 72%,#4e8a3c 100%)}
.quote{position:absolute;left:190px;width:820px;font-style:italic;font-size:14px;line-height:22px;color:var(--muted)}
.quote.q1{top:572px}.quote.q2{top:664px}

/* cta */
.cta{height:392px;text-align:center}
.cta .photo{inset:0;background:linear-gradient(180deg,#2f2f2f,#3a342d 60%,#4a3f32 100%)}
.cta h2{position:relative;padding-top:64px;font-family:"Lato",sans-serif;font-weight:700;font-size:30px;line-height:40px;color:var(--white)}
.cta p{position:relative;margin-top:14px;font-size:17px;color:var(--white)}
.cta-form{position:absolute;top:254px;left:206px;width:788px;display:flex;gap:14px}
.cta-form span{flex:1;height:44px;background:#eef8fc;border:1px solid #c9e8f3;text-align:left;padding:12px 14px;font-size:14px;color:#6b7780}
.cta-btn{position:absolute;top:320px;left:521px;width:158px;height:40px;border-radius:20px;background:var(--teal);color:var(--white);font-family:"Lato",sans-serif;font-weight:700;font-size:14px;line-height:40px;letter-spacing:1px}

/* footer */
.site-footer{height:77px;background:var(--teal);text-align:center;font-size:13px;line-height:77px;color:#d8f1fa}
</style>
</head>
<body>

<header class="site-header">
  <div class="brand"><span class="brand-dot"></span>VERDANT HOLLOW</div>
  <div class="header-contact"><span class="call">Call Us Now On :</span> 555-014-2290<br>Client Portal | Get A Free Quote</div>
</header>
<nav class="main-nav">
  <a href="#">HOME</a><a href="#">ABOUT US</a><a href="#">RESIDENTIAL</a><a href="#">COMMERCIAL</a><a href="#">BLOG</a><a href="#">CONTACT US</a>
</nav>

<section class="hero">
  <div class="photo hero-bg" role="img" aria-label="Tropical bay with palm trees, green mountains and turquoise water"></div>
  <h1 class="hero-title">VERDANT HOLLOW</h1>
  <p class="hero-lead">You don't have an abundance of free time. And, you simply don't want to spend the little time you have – mowing a lawn and pruning the plants.</p>
  <div class="dots"><span class="on"></span><span></span><span></span><span></span></div>
  <svg class="hero-wave" width="1200" height="90" viewBox="0 0 1200 90">
    <path d="M0 40 C300 90 700 0 1200 30 L1200 90 L0 90Z" fill="#9aa3aa" opacity=".6"/>
    <path d="M0 55 C320 95 720 20 1200 45 L1200 90 L0 90Z" fill="#ffffff"/>
  </svg>
</section>

<section class="intro">
  <p class="intro-text">You would probably like to spend that time the way you should, instead. Enjoying the sunset in the privacy of your garden, watching a favorite TV show while lying on a hammock, or throwing an occasional BBQ party with your friends and loved ones. Right?</p>
  <div class="photo photo-beach" role="img" aria-label="Beachfront villa on a sandy shore"></div>
  <div class="photo photo-cove" role="img" aria-label="Turquoise cove lined with trees and white houses"></div>
</section>

<section class="coast-band">
  <div class="photo" role="img" aria-label="Aerial view of a coastal town and harbour"></div>
  <p>Getting an outdoor area of your dreams is not that difficult, nor expensive. You can make this happen by getting a help from a landscaping company that offers tailor-made services.</p>
</section>

<section class="compare">
  <article class="card card-generic">
    <div class="photo" role="img" aria-label="Palm tree garden above the sea"></div>
    <div class="card-body">
      <h2>Generic landscaping services</h2>
      <ul>
        <li><svg width="14" height="14" viewBox="0 0 14 14"><circle cx="7" cy="7" r="7" fill="#1aa5cf"/><path d="M3.8 7.2l2.2 2.2 4.2-4.4" stroke="#fff" stroke-width="1.6" fill="none"/></svg>You pay for the bundle of services, regardless of whether you actually need them</li>
        <li><svg width="14" height="14" viewBox="0 0 14 14"><circle cx="7" cy="7" r="7" fill="#1aa5cf"/><path d="M3.8 7.2l2.2 2.2 4.2-4.4" stroke="#fff" stroke-width="1.6" fill="none"/></svg>You get a generic service, not adjusted to the specific needs of your outdoor area</li>
        <li><svg width="14" height="14" viewBox="0 0 14 14"><circle cx="7" cy="7" r="7" fill="#1aa5cf"/><path d="M3.8 7.2l2.2 2.2 4.2-4.4" stroke="#fff" stroke-width="1.6" fill="none"/></svg>The field team thinks of your property as just another task they have to complete</li>
      </ul>
    </div>
  </article>
  <article class="card card-tailored">
    <div class="photo" role="img" aria-label="Family house with a trimmed front lawn"></div>
    <div class="card-body">
      <h2>Tailor-made landscaping services</h2>
      <ul>
        <li><svg width="14" height="14" viewBox="0 0 14 14"><circle cx="7" cy="7" r="7" fill="#1aa5cf"/><path d="M3.8 7.2l2.2 2.2 4.2-4.4" stroke="#fff" stroke-width="1.6" fill="none"/></svg>You pay only for the services your yard really needs.</li>
        <li><svg width="14" height="14" viewBox="0 0 14 14"><circle cx="7" cy="7" r="7" fill="#1aa5cf"/><path d="M3.8 7.2l2.2 2.2 4.2-4.4" stroke="#fff" stroke-width="1.6" fill="none"/></svg>You get your garden's specific issues solved, and specific requirements met</li>
        <li><svg width="14" height="14" viewBox="0 0 14 14"><circle cx="7" cy="7" r="7" fill="#1aa5cf"/><path d="M3.8 7.2l2.2 2.2 4.2-4.4" stroke="#fff" stroke-width="1.6" fill="none"/></svg>The field team members take their time working on your property</li>
        <li><svg width="14" height="14" viewBox="0 0 14 14"><circle cx="7" cy="7" r="7" fill="#1aa5cf"/><path d="M3.8 7.2l2.2 2.2 4.2-4.4" stroke="#fff" stroke-width="1.6" fill="none"/></svg>They get to learn all about your vision – and make it a reality</li>
      </ul>
    </div>
  </article>
</section>

<section class="eco-band">
  <div class="photo" role="img" aria-label="Large manicured lawn in front of a house at dusk"></div>
  <h2>Why should you care that Verdant Hollow employs the leading industry experts and uses modern, eco-friendly technical solutions?</h2>
  <p>That is why we're able to transform your lawn into a green carpet and get your plants in a perfect health. All while keeping your vision and your budget on our minds. That is why our services actually enable you to reduce the operating expenses.</p>
</section>

<section class="benefits">
  <h2>More benefits of having a well-maintained yard</h2>
  <div class="benefit b1">
    <div class="icon"><svg width="44" height="40" viewBox="0 0 44 40"><rect x="2" y="2" width="40" height="36" fill="none" stroke="#fff" stroke-width="3"/><rect x="10" y="20" width="5" height="13" fill="#fff"/><rect x="19" y="12" width="5" height="21" fill="#fff"/><rect x="28" y="16" width="5" height="17" fill="#fff"/></svg></div>
    In some cases, a great looking lawn can increase your property's value up to 20%.
  </div>
  <div class="benefit b2">
    <div class="icon"><svg width="46" height="40" viewBox="0 0 46 40"><path d="M23 3L3 21h6v17h10V27h8v11h10V21h6Z" fill="#fff"/></svg></div>
    Your lawn and plants reduce the energy consumption – countering the warming effects of paved surfaces.
  </div>
  <div class="benefit b3">
    <div class="icon"><svg width="40" height="40" viewBox="0 0 40 40"><path d="M3 4h34L24 21v15l-8-4V21Z" fill="#fff"/></svg></div>
    They act as giant dust filters, increasing air quality, and removing carbon dioxide from the atmosphere
  </div>
</section>

<section class="flaws">
  <div class="photo" role="img" aria-label="Blue sea with a hillside mansion on the right"></div>
  <h2>Do our services have flaws?<br>Yes. They have two giant ones.</h2>
  <ol>
    <li>1. Your "new" garden will get all of your neighbors jealous.</li>
    <li>2. Your friends will probably start inviting themselves over more frequently.</li>
  </ol>
</section>

<section class="testimonials">
  <h2>At Verdant Hollow, we do more than just keeping your<br>landscape in a pristine state</h2>
  <div class="photo" role="img" aria-label="White two-storey mansion surrounded by palm trees and lawn"></div>
  <p class="quote q1">"We are delighted with your landscaping, both with the design and implementation.It's not very often these days that work exceeds expectations."</p>
  <p class="quote q2">"Verdant Hollow are efficient, on-time, responsive, provide fair pricing, do outstanding work, have great people, and actually follow up on their work."</p>
</section>

<section class="cta">
  <div class="photo" role="img" aria-label="Dim patio with lounge chairs"></div>
  <h2>So, what's the next step to enriching your living area?<br>And getting you a garden from your dreams.</h2>
  <p>It's simple, just book a no-obligations consultation</p>
  <div class="cta-form"><span>Name</span><span>Email Address</span></div>
  <div class="cta-btn">GET STARTED</div>
</section>

<footer class="site-footer">Copyright 2017 Verdant Hollow All Rights Reserved</footer>

</body>
</html>
```